HML5 Web Application Design

We need a graphic design to give a HTML web application a modern look and feel. The design should be clean and neat with a metro inspired interface. All application uses vandrix controls so any experience with these would be great.
Perhaps you could also include a few screenshots of your previous work

Industry/Entity Type

Graphic Design

Requirements
Must have
• Must be HTML 5 compliant

```html
<!DOCTYPE html>
<html lang="en">
<head>
<meta charset="utf-8">
<title>Supplier Transactions Screen</title>
<link href="https://fonts.googleapis.com/css2?family=Barlow:wght@400;500;600;700&display=swap" rel="stylesheet">
<style>
:root{
  --page:#d8d8d8;
  --bar:#111111;
  --side:#e1e1e1;
  --white:#ffffff;
  --orange:#f26522;
  --blue:#0088c0;
  --grey-head:#666666;
  --row-alt:#ebebeb;
  --text:#555555;
  --dark:#222222;
  --link:#0a8cc4;
  --t-user:#a1003d;
  --t-setting:#a03500;
  --t-support:#7ba200;
  --t-events:#17a100;
  --t-graph:#00a19b;
  --t-docs:#0056a2;
  --t-msg:#a07a00;
  --t-source:#f26522;
  --t-refresh:#3e0f69;
  --t-library:#e9008b;
}
*{box-sizing:border-box;margin:0;padding:0}
html,body{width:1200px;height:1000px;overflow:hidden}
body{background:var(--page);font-family:"Barlow",sans-serif;position:relative;color:var(--text)}
.app{position:absolute;left:96px;top:88px;width:1000px;height:824px;background:var(--white)}
.topbar{position:absolute;left:0;top:0;width:1000px;height:51px;background:var(--bar)}
.brand{position:absolute;left:34px;top:9px;display:flex;align-items:center;gap:10px;color:#fff;font-weight:700;font-size:34px;letter-spacing:-.5px;line-height:34px;white-space:nowrap}
.brand-dot{width:22px;height:22px;border-radius:50%;background:var(--orange)}
.mainnav{position:absolute;left:0;top:15px;width:1000px;height:22px;list-style:none;font-size:15px;color:#fff;font-weight:400}
.mainnav li{position:absolute;top:0;height:22px;line-height:22px;white-space:nowrap}
.mainnav li.active{background:var(--orange);width:80px;text-align:center}
.mainnav .caret{font-size:10px;vertical-align:2px;margin-left:3px}
.sidebar{position:absolute;left:0;top:51px;width:333px;height:773px;background:var(--side)}
.avatar{position:absolute;left:19px;top:25px;width:85px;height:86px;border:3px solid #bdbdbd;background:#f4f4f4;display:block}
.avatar span{position:absolute;inset:4px;background:linear-gradient(#e9e9e9,#c7c7c7)}
.greeting{position:absolute;left:115px;top:25px;font-size:12px;line-height:17px;color:var(--dark);white-space:nowrap}
.greeting strong{display:block;font-weight:600;font-size:13px;text-transform:uppercase;margin-bottom:1px}
.accent-rule{position:absolute;left:0;top:135px;width:320px;height:6px;background:var(--orange)}
.search{position:absolute;left:21px;top:155px;width:298px;height:40px;border:1px solid #c8c8c8;background:#fff}
.search span{position:absolute;left:13px;top:9px;font-size:17px;color:#aaa}
.search-btn{position:absolute;right:-1px;top:-1px;width:40px;height:40px;background:#5a5a5a}
.rail{position:absolute;left:0;top:210px;width:97px;height:527px;background:var(--blue)}
.rail svg{position:absolute;left:32px;width:34px;height:34px}
.tile{position:absolute;width:83px;height:83px;color:#fff;font-size:12px;font-weight:400;text-align:center;white-space:nowrap}
.tile svg{position:absolute;left:24px;top:14px;width:36px;height:36px}
.tile .label{position:absolute;left:0;right:0;bottom:6px;line-height:14px}
.badge{position:absolute;right:0;top:0;background:#7a0030;font-size:12px;padding:0 3px;line-height:17px}
.content{position:absolute;left:358px;top:51px;width:642px}
.title{position:absolute;left:0;top:10px;font-size:25px;font-weight:400;color:#5a5a5a;letter-spacing:.3px;line-height:30px;white-space:nowrap}
.title-rule{position:absolute;left:0;top:48px;width:642px;height:1px;background:#ddd}
.crumbs{position:absolute;left:4px;top:54px;font-size:16px;line-height:20px;color:#333;display:flex;align-items:center;gap:8px}
.crumbs .current{color:var(--link)}
.filters{position:absolute;left:0;top:78px;width:642px;height:39px;background:#e6e6e6;font-size:16px}
.filters label{position:absolute;top:9px;line-height:20px}
.date-input{position:absolute;top:7px;width:172px;height:26px;background:#fff;border:1px solid #c8c8c8;color:#aaa;font-size:16px;text-align:center;line-height:24px;padding-right:22px}
.date-input i{position:absolute;right:-1px;top:-1px;width:25px;height:26px;background:var(--orange)}
.table-wrap{position:absolute;left:0;top:135px;width:642px;border-top:6px solid var(--orange)}
table{border-collapse:collapse;width:642px;table-layout:fixed;font-size:14px}
th{background:var(--grey-head);color:#fff;font-weight:400;font-size:16px;text-align:left;height:37px;line-height:16px;padding:0 0 0 8px;border-right:1px solid #777;position:relative;white-space:nowrap}
th::after{content:"";position:absolute;right:7px;top:14px;border:5px solid transparent;border-top:7px solid #fff}
th.dim::after{border-top-color:#999}
td{height:34px;line-height:14px;padding:0 0 0 8px;color:#555;white-space:nowrap}
tbody tr:nth-child(even) td{background:var(--row-alt)}
.pager{position:absolute;left:0;top:696px;width:642px;height:38px;background:var(--grey-head);font-size:12px;color:#bbb}
.pager .count{position:absolute;left:367px;top:12px;line-height:14px}
.pg{position:absolute;top:7px;width:28px;height:26px;background:#2a2a2a;color:#fff}
.pg.current{background:#fff;color:var(--orange);text-align:center;line-height:26px;font-size:16px;width:30px}
.footer{position:absolute;left:0;top:752px;width:642px;height:21px;background:#000;color:#fff;font-size:10px;line-height:21px;padding-left:6px;letter-spacing:.1px;white-space:nowrap;overflow:hidden}
</style>
</head>
<body>
<div class="app">
  <header class="topbar">
    <div class="brand">ORVEN<span class="brand-dot"></span></div>
    <ul class="mainnav">
      <li style="left:216px">HOME</li>
      <li style="left:274px">PIN REQUESTS</li>
      <li style="left:388px">TRANSECTIONS</li>
      <li style="left:507px">TAX DETAILS</li>
      <li style="left:608px">USERS</li>
      <li style="left:670px">SUPLIERS</li>
      <li class="active" style="left:750px">QUEIRES</li>
      <li style="left:849px">LA STAFF QUEIRES<span class="caret">▼</span></li>
    </ul>
  </header>

  <aside class="sidebar">
    <div class="avatar" role="img" aria-label="User profile photo placeholder"><span></span></div>
    <div class="greeting"><strong>Hello Mirel Ostand</strong>Edit Profile<br>View Profile<br>Logout</div>
    <div class="accent-rule"></div>
    <div class="search"><span>Search Here</span>
      <div class="search-btn"><svg width="40" height="40" viewBox="0 0 40 40"><circle cx="23" cy="17" r="7" fill="none" stroke="#fff" stroke-width="2"/><line x1="18" y1="22" x2="11" y2="29" stroke="#fff" stroke-width="3"/></svg></div>
    </div>

    <nav class="rail">
      <svg style="top:28px" viewBox="0 0 34 34"><circle cx="17" cy="11" r="6" fill="#fff"/><path d="M6 32c0-9 4-13 11-13s11 4 11 13z" fill="#fff"/></svg>
      <svg style="top:100px" viewBox="0 0 34 34"><circle cx="12" cy="15" r="8" fill="none" stroke="#fff" stroke-width="5" stroke-dasharray="3 2"/><circle cx="12" cy="15" r="5" fill="#fff"/><circle cx="12" cy="15" r="2" fill="var(--blue)"/><circle cx="26" cy="22" r="4" fill="#fff"/></svg>
      <svg style="top:173px" viewBox="0 0 34 34"><circle cx="17" cy="17" r="14" fill="#fff"/><circle cx="17" cy="17" r="6" fill="var(--blue)"/><path d="M17 3v8M17 23v8M3 17h8M23 17h8" stroke="var(--blue)" stroke-width="3"/></svg>
      <svg style="top:245px" viewBox="0 0 34 34"><path d="M15 5a13 13 0 1 0 13 13H15z" fill="none" stroke="#fff" stroke-width="3"/><path d="M18 2v13h13A13 13 0 0 0 18 2z" fill="#fff"/></svg>
      <svg style="top:318px" viewBox="0 0 34 34"><rect x="2" y="8" width="30" height="20" fill="#fff"/><path d="M2 8l15 11 15-11" fill="none" stroke="var(--blue)" stroke-width="2"/></svg>
      <svg style="top:394px" viewBox="0 0 34 34"><circle cx="17" cy="17" r="15" fill="#fff"/><path d="M11 17a6 6 0 1 0 3-5" fill="none" stroke="var(--blue)" stroke-width="3"/><path d="M10 9v5h5" fill="var(--blue)"/></svg>
      <svg style="top:464px" viewBox="0 0 34 34"><rect x="3" y="5" width="28" height="24" fill="none" stroke="#fff" stroke-width="2"/><line x1="3" y1="10" x2="31" y2="10" stroke="#fff" stroke-width="2"/><path d="M13 15l-4 4 4 4M21 15l4 4-4 4M18 14l-2 10" fill="none" stroke="#fff" stroke-width="1.6"/></svg>
    </nav>

    <div class="tile" style="left:121px;top:210px;background:var(--t-user)"><span class="badge">15</span><svg viewBox="0 0 36 36"><circle cx="18" cy="11" r="6" fill="#fff"/><path d="M8 32c0-9 4-13 10-13s10 4 10 13z" fill="#fff"/></svg><span class="label">USER</span></div>
    <div class="tile" style="left:231px;top:210px;background:var(--t-setting)"><svg viewBox="0 0 36 36"><circle cx="13" cy="17" r="8" fill="none" stroke="#fff" stroke-width="5" stroke-dasharray="3 2"/><circle cx="13" cy="17" r="5" fill="#fff"/><circle cx="28" cy="23" r="4" fill="#fff"/></svg><span class="label">SETTING</span></div>
    <div class="tile" style="left:121px;top:321px;background:var(--t-support)"><svg viewBox="0 0 36 36"><circle cx="18" cy="18" r="15" fill="#fff"/><circle cx="18" cy="18" r="7" fill="var(--t-support)"/><path d="M18 3v8M18 25v8M3 18h8M25 18h8" stroke="var(--t-support)" stroke-width="3"/></svg><span class="label">SUPPORT</span></div>
    <div class="tile" style="left:231px;top:321px;background:var(--t-events)"><svg viewBox="0 0 36 36"><path d="M22 3c-8 6-10 16-8 24l-2 6h2l2-5c6-5 8-15 6-25z" fill="#fff"/></svg><span class="label">EVENTS</span></div>
    <div class="tile" style="left:121px;top:432px;background:var(--t-graph)"><svg viewBox="0 0 36 36"><path d="M16 6a13 13 0 1 0 13 13H16z" fill="none" stroke="#fff" stroke-width="3"/><path d="M19 3v13h13A13 13 0 0 0 19 3z" fill="#fff"/></svg><span class="label">GRAPH</span></div>
    <div class="tile" style="left:231px;top:432px;background:var(--t-docs)"><svg viewBox="0 0 36 36"><path d="M2 8h9v16H2zM13 8h9v16h-9zM24 8h9v16h-9z" fill="none" stroke="#fff" stroke-width="2"/></svg><span class="label">DOUCOMENTS</span></div>
    <div class="tile" style="left:121px;top:543px;background:var(--t-msg)"><svg viewBox="0 0 36 36"><rect x="1" y="7" width="34" height="22" fill="#fff"/><path d="M1 7l17 12 17-12" fill="none" stroke="var(--t-msg)" stroke-width="2"/></svg><span class="label">MASSAGE</span></div>
    <div class="tile" style="left:231px;top:543px;background:var(--t-source)"><svg viewBox="0 0 36 36"><rect x="4" y="7" width="28" height="22" fill="none" stroke="#fff" stroke-width="2"/><line x1="4" y1="12" x2="32" y2="12" stroke="#fff" stroke-width="2"/><path d="M14 16l-4 4 4 4M22 16l4 4-4 4M19 15l-2 10" fill="none" stroke="#fff" stroke-width="1.6"/></svg><span class="label">SOURCE</span></div>
    <div class="tile" style="left:121px;top:654px;background:var(--t-refresh)"><svg viewBox="0 0 36 36"><circle cx="18" cy="18" r="16" fill="#fff"/><path d="M12 18a6 6 0 1 0 3-5" fill="none" stroke="var(--t-refresh)" stroke-width="3"/><path d="M11 10v5h5" fill="var(--t-refresh)"/></svg><span class="label">REFRESH</span></div>
    <div class="tile" style="left:231px;top:654px;background:var(--t-library)"><svg viewBox="0 0 36 36"><rect x="3" y="4" width="30" height="28" fill="none" stroke="#fff" stroke-width="2"/><line x1="3" y1="17" x2="33" y2="17" stroke="#fff" stroke-width="2"/><path d="M8 7v8M12 7v8M21 20v10M25 20v10M29 20v10M8 20v10" stroke="#fff" stroke-width="2"/></svg><span class="label">LIBRARY</span></div>
  </aside>

  <main class="content">
    <h1 class="title">Supliar Transactions Screen</h1>
    <div class="title-rule"></div>
    <div class="crumbs">
      <svg width="18" height="16" viewBox="0 0 18 16"><path d="M9 1l8 7h-2v7h-4v-4H7v4H3V8H1z" fill="var(--link)"/></svg>
      <span>›</span><span>Login</span><span>›</span><span class="current">Data</span>
    </div>
    <div class="filters">
      <label style="left:7px">Date From</label>
      <div class="date-input" style="left:92px">8/8/2013<i><svg width="25" height="26" viewBox="0 0 25 26"><rect x="5" y="7" width="15" height="13" fill="none" stroke="#fff" stroke-width="1.5"/><path d="M5 11h15" stroke="#fff" stroke-width="2"/></svg></i></div>
      <label style="left:277px">Date to</label>
      <div class="date-input" style="left:362px">9/8/2013<i><svg width="25" height="26" viewBox="0 0 25 26"><rect x="5" y="7" width="15" height="13" fill="none" stroke="#fff" stroke-width="1.5"/><path d="M5 11h15" stroke="#fff" stroke-width="2"/></svg></i></div>
    </div>

    <div class="table-wrap">
      <table>
        <colgroup><col style="width:97px"><col style="width:102px"><col style="width:97px"><col style="width:147px"><col style="width:98px"><col style="width:101px"></colgroup>
        <thead><tr><th class="dim">DATE</th><th>TYPE</th><th>TIME</th><th>REFRENCE</th><th>AMOUNT</th><th>STETUS</th></tr></thead>
        <tbody>
          <tr><td>03/01/2013</td><td>INV</td><td>03:02 AM</td><td>2548788AAC</td><td>500.00</td><td>RECIVED</td></tr>
          <tr><td>03/01/2013</td><td>PAYMENT</td><td>03:02 AM</td><td>2548788AAC</td><td>100.00</td><td>PAYMENT</td></tr>
          <tr><td>03/01/2013</td><td>PAYMENT</td><td>03:02 AM</td><td>2548788AAC</td><td>100.00</td><td>PAYMENT</td></tr>
          <tr><td>03/01/2013</td><td>PAYMENT</td><td>03:02 AM</td><td>2548788AAC</td><td>100.00</td><td>PAYMENT</td></tr>
          <tr><td>03/01/2013</td><td>PAYMENT</td><td>03:02 AM</td><td>2548788AAC</td><td>100.00</td><td>PAYMENT</td></tr>
          <tr><td>03/01/2013</td><td>INV</td><td>03:02 AM</td><td>2548788AAC</td><td>500.00</td><td>RECIVED</td></tr>
          <tr><td>03/01/2013</td><td>INV</td><td>03:02 AM</td><td>2548788AAC</td><td>500.00</td><td>RECIVED</td></tr>
          <tr><td>03/01/2013</td><td>INV</td><td>03:02 AM</td><td>2548788AAC</td><td>500.00</td><td>RECIVED</td></tr>
          <tr><td>03/01/2013</td><td>INV</td><td>03:02 AM</td><td>2548788AAC</td><td>500.00</td><td>RECIVED</td></tr>
          <tr><td>03/01/2013</td><td>INV</td><td>03:02 AM</td><td>2548788AAC</td><td>500.00</td><td>RECIVED</td></tr>
          <tr><td>03/01/2013</td><td>INV</td><td>03:02 AM</td><td>2548788AAC</td><td>500.00</td><td>RECIVED</td></tr>
          <tr><td>03/01/2013</td><td>INV</td><td>03:02 AM</td><td>2548788AAC</td><td>500.00</td><td>RECIVED</td></tr>
          <tr><td>03/01/2013</td><td>INV</td><td>03:02 AM</td><td>2548788AAC</td><td>500.00</td><td>RECIVED</td></tr>
          <tr><td>03/01/2013</td><td>INV</td><td>03:02 AM</td><td>2548788AAC</td><td>500.00</td><td>RECIVED</td></tr>
          <tr><td>03/01/2013</td><td>INV</td><td>03:02 AM</td><td>2548788AAC</td><td>500.00</td><td>RECIVED</td></tr>
        </tbody>
      </table>
    </div>

    <div class="pager">
      <span class="count">1-2 OF 2 ITEMS</span>
      <div class="pg" style="left:469px"><svg width="28" height="26" viewBox="0 0 28 26"><path d="M13 8l-5 5 5 5M20 8l-5 5 5 5" fill="none" stroke="#fff" stroke-width="2.5"/></svg></div>
      <div class="pg" style="left:504px"><svg width="28" height="26" viewBox="0 0 28 26"><path d="M16 9l-4 4 4 4" fill="none" stroke="#fff" stroke-width="2"/></svg></div>
      <div class="pg current" style="left:537px">2</div>
      <div class="pg" style="left:573px"><svg width="28" height="26" viewBox="0 0 28 26"><path d="M12 9l4 4-4 4" fill="none" stroke="#fff" stroke-width="2"/></svg></div>
      <div class="pg" style="left:607px"><svg width="28" height="26" viewBox="0 0 28 26"><path d="M8 8l5 5-5 5M15 8l5 5-5 5" fill="none" stroke="#fff" stroke-width="2.5"/></svg></div>
    </div>

    <footer class="footer">COPYRIGHT © 2013 KOVARI. ALL PAGES OF THE WEBSITE ARE SUBJECT TO OUR TERMS AND CONDITIONS AND PRIVACY POLICY.</footer>
  </main>
</div>
</body>
</html>
```